Website Design - Financial Services Software

We are looking for website designs for our public website.
Some competitor sites we like are
www.torvani.com.au
www.pluma.com.au
www.quentabridge.com
www.morlupa.com.au

A wireframe example of our site can be found at
http://pr4tqz.bivlowpage.com/

Attached is our logo.

Industry/Entity Type

Financial

```html
<!DOCTYPE html>
<html lang="en">
<head>
<meta charset="utf-8">
<title>Velmora – Smarter Financial Strategies</title>
<link rel="stylesheet" href="https://fonts.googleapis.com/css2?family=Noto+Serif:wght@400;700&family=Source+Sans+3:wght@400;600&display=swap">
<style>
:root{
  --gold:#c0901c;
  --gold-light:#d9b344;
  --gold-dark:#a97c12;
  --ink:#555;
  --ink-dark:#333;
  --hero-bg:#eeeeee;
  --footer-bg:#3a3a3a;
  --footer-text:#a8a8a8;
  --white:#fff;
}
*{margin:0;padding:0;box-sizing:border-box}
html,body{width:1200px;height:1200px;overflow:hidden;background:var(--white)}
body{position:relative;font-family:"Source Sans 3",Arial,sans-serif;color:var(--ink)}
.abs{position:absolute}

/* header */
.brand{left:130px;top:30px;display:flex;align-items:center;gap:8px}
.brand-mark{width:14px;height:14px;border-radius:50%;background:var(--gold)}
.brand-name{font-family:"Noto Serif",Georgia,serif;font-size:22px;color:var(--gold);letter-spacing:1px}
.login{left:990px;top:19px;width:78px;height:31px;background:linear-gradient(#e6c45a,#cfa430);border:1px solid #b9911e;border-radius:2px;color:#4a3a10;font-size:13px;display:flex;align-items:center;justify-content:center;gap:6px}
.nav{left:678px;top:74px;width:390px;display:flex;justify-content:space-between;font-size:12.5px;color:#444}
.nav .active{color:var(--gold)}

/* hero */
.hero{left:0;top:114px;width:1200px;height:424px;background:var(--hero-bg);box-shadow:0 6px 10px -8px rgba(0,0,0,.25)}
.hero-title{left:132px;top:160px;font-family:"Noto Serif",Georgia,serif;font-weight:700;font-size:37px;line-height:46px;color:var(--gold)}
.hero-sub{left:132px;top:271px;font-size:19.5px;line-height:30px;color:#444}
.card{width:220px;height:126px;border:3px solid #d4d4d4;background:#c8ced6}
.card .label{position:absolute;left:0;right:0;bottom:0;height:34px;background:rgba(40,40,40,.72);color:var(--white);font-size:15.5px;display:flex;align-items:center;justify-content:center}
.card-planning{left:130px;top:364px;background:linear-gradient(135deg,#e9edf2,#b9c4d2)}
.card-dealer{left:368px;top:364px;background:linear-gradient(135deg,#d7dde3,#7f98b4)}
.video{left:610px;top:150px;width:460px;height:344px;border:4px solid #d0d0d0;background:linear-gradient(135deg,#efe8dc,#c9b49a 60%,#8c6c4c)}
.video-play{left:190px;top:134px}
.controls-play{left:10px;top:284px;width:62px;height:38px;background:rgba(40,40,40,.85);border-radius:3px;display:flex;align-items:center;justify-content:center}
.controls-bar{left:81px;top:284px;width:359px;height:38px;background:rgba(40,40,40,.85);border-radius:3px}
.progress{left:12px;top:14px;width:243px;height:10px;border:1px solid #888;background:#555}
.progress span{display:block;width:52%;height:100%;background:#bbb}
.hd{left:296px;top:9px;color:#2ea3e6;font-weight:600;font-style:italic;font-size:14px}

/* intro */
.intro-title{left:132px;top:618px;font-family:"Noto Serif",Georgia,serif;font-weight:700;font-size:24px;color:var(--gold)}
.intro-text{left:132px;width:380px;font-size:12.5px;line-height:20px;color:#666}
.p1{top:666px}
.p2{top:728px}
.read-more{left:132px;top:826px;width:94px;height:31px;background:linear-gradient(#d6ab3c,#c0901c);border-radius:2px;color:var(--white);font-size:13px;display:flex;align-items:center;justify-content:center}
.tile{width:167px;height:102px}
.t1{left:531px;top:620px;background:linear-gradient(#2d4a60,#1f3447)}
.t2{left:718px;top:620px;background:linear-gradient(135deg,#f3e6dc,#d63b3b 50%,#e9dbd0)}
.t3{left:902px;top:620px;background:linear-gradient(135deg,#a7b8cc,#dfe5ec 60%,#c59f87)}
.t4{left:531px;top:743px;background:linear-gradient(135deg,#e9c3a3,#f2ede8 60%,#9fb8c4)}
.t5{left:718px;top:743px;background:linear-gradient(#e8c7a6,#d9a475 70%,#b88a5a)}
.t6{left:902px;top:743px;background:linear-gradient(#f6efc2,#f3e9b0)}

/* cta */
.cta{left:129px;top:910px;width:942px;height:74px;background:linear-gradient(#dcb84a,#c79b25);border:1px solid #b58a18}
.cta-text{left:55px;top:20px;font-family:"Noto Serif",Georgia,serif;font-size:23.5px;color:#3a3020}
.cta-btn{left:717px;top:19px;width:168px;height:38px;background:linear-gradient(#555,#383838);border:1px solid #2a2a2a;border-radius:2px;color:var(--white);font-size:14px;display:flex;align-items:center;justify-content:center}

/* footer */
.footer{left:0;top:1033px;width:1200px;height:167px;background:var(--footer-bg)}
.footer-brand{left:140px;top:82px;display:flex;align-items:center;gap:8px}
.footer-brand .brand-mark{background:var(--white)}
.footer-brand .brand-name{color:var(--white)}
.fcol{top:25px}
.fcol h4{font-weight:400;font-size:13.5px;color:var(--white);margin-bottom:10px}
.fcol a{display:block;color:var(--footer-text);font-size:12px;line-height:19px;text-decoration:none}
.c-about{left:414px}
.c-start{left:550px}
.c-legal{left:737px}
.c-connect{left:878px}
.social{display:flex;align-items:center;gap:9px;color:var(--footer-text);font-size:12px;height:24px;margin-bottom:13px}
.social i{width:24px;height:24px;border-radius:50%;background:#888;display:block}
.copyright{left:132px;top:140px;font-size:11.5px;color:var(--footer-text)}
</style>
</head>
<body>

<header>
  <div class="abs brand"><span class="brand-mark"></span><span class="brand-name">VELMORA</span></div>
  <div class="abs login">
    <svg width="12" height="12" viewBox="0 0 12 12"><path d="M2 11 L10 2" stroke="#4a3a10" stroke-width="2"/></svg>LOGIN
  </div>
  <nav class="abs nav">
    <span class="active">HOME</span><span>/</span><span>FEATURED</span><span>/</span><span>EXAMPLES</span><span>/</span><span>FAQ</span><span>/</span><span>ABOUT</span>
  </nav>
</header>

<section class="abs hero">
</section>
<h1 class="abs hero-title">SMARTER<br>FINANCIAL STRATEGIES</h1>
<p class="abs hero-sub">Values and Cash-flow focused financial software<br>for financial planners.</p>

<div class="abs card card-planning" role="img" aria-label="Photo of hands reviewing financial charts with a pen">
  <div class="label">FOR PLANNING PRACTICES</div>
</div>
<div class="abs card card-dealer" role="img" aria-label="Photo of a smiling businessman in an office">
  <div class="label">FOR DEALER GROUPS</div>
</div>

<div class="abs video" role="img" aria-label="Video still of a coffee cup and a napkin sketch of personal financial planning topics">
  <svg class="abs video-play" width="80" height="80" viewBox="0 0 80 80">
    <circle cx="40" cy="40" r="37" fill="rgba(40,40,40,.65)"/>
    <path d="M31 24 L57 40 L31 56 Z" fill="rgba(255,255,255,.75)"/>
  </svg>
  <div class="abs controls-play">
    <svg width="16" height="18" viewBox="0 0 16 18"><path d="M1 1 L15 9 L1 17 Z" fill="#fff"/></svg>
  </div>
  <div class="abs controls-bar">
    <div class="abs progress"><span></span></div>
    <svg class="abs" style="left:268px;top:12px" width="28" height="14" viewBox="0 0 28 14">
      <g fill="#2ea3e6"><rect x="0" y="0" width="3" height="14"/><rect x="5" y="0" width="3" height="14"/><rect x="10" y="0" width="3" height="14"/><rect x="15" y="0" width="3" height="14"/><rect x="20" y="0" width="3" height="14"/><rect x="25" y="0" width="3" height="14"/></g>
    </svg>
    <span class="abs hd">HD</span>
    <svg class="abs" style="left:330px;top:11px" width="16" height="16" viewBox="0 0 16 16"><rect x="2" y="2" width="12" height="12" fill="none" stroke="#ddd" stroke-width="1.5"/></svg>
  </div>
</div>

<section>
  <h2 class="abs intro-title">LOREM IPSUM DOLOR</h2>
  <p class="abs intro-text p1">Lorem ipsum dolor sit amet, consectetur adipiscing elit. Morbi dapi-bus justo vel felis volutpat, sit amet.</p>
  <p class="abs intro-text p2">Maecenas vehicula justo et mauris tempus, vel dignissim doloraliquet. Maecenas erat metus, scelerisque eget placerat gravida, consectetur fermentum magna. Aenean elementum hendrerit turpis nec sodales fermentum magna scelerisque</p>
  <div class="abs read-more">Read More</div>

  <div class="abs tile t1" role="img" aria-label="Photo of a row of piggy banks"></div>
  <div class="abs tile t2" role="img" aria-label="Photo of hands assembling red puzzle pieces spelling strategy"></div>
  <div class="abs tile t3" role="img" aria-label="Photo of hands holding a smartphone"></div>
  <div class="abs tile t4" role="img" aria-label="Photo of a smiling support agent with a headset"></div>
  <div class="abs tile t5" role="img" aria-label="Photo of a hand stacking coins"></div>
  <div class="abs tile t6" role="img" aria-label="Illustration of people on a rising chart arrow"></div>
</section>

<div class="abs cta">
  <p class="abs cta-text">Create an account today and begin your 30 day trial!</p>
  <div class="abs cta-btn">Sign Up Now !</div>
</div>

<footer class="abs footer">
  <div class="abs footer-brand"><span class="brand-mark"></span><span class="brand-name">VELMORA</span></div>
  <div class="abs fcol c-about"><h4>ABOUT</h4><a>About Us</a><a>Support</a></div>
  <div class="abs fcol c-start"><h4>GETTING STARTED</h4><a>Why Velmora</a><a>Download a Summary</a><a>Velmora Videos</a></div>
  <div class="abs fcol c-legal"><h4>LEGAL</h4><a>Terms of Use</a><a>Privacy</a></div>
  <div class="abs fcol c-connect"><h4>CONNECT</h4>
    <div class="social"><i></i>Velmora on Linkora</div>
    <div class="social"><i></i>Velmora on Chirpnet</div>
  </div>
  <p class="abs copyright">© 2014 Velmora Pty Ltd. All rights reserved.</p>
</footer>

</body>
</html>
```